Corvelle Strategies business card

I need a business card for my new strategic consulting LLC, Corvelle Strategies. We specialize in helping people who care about broadband technology and telecommunications policy, and we're based in Washington DC. I'm looking for a card that says smart, credible, future-facing and signals a high level of expertise. It's DC, so there's clearly a limit to how crazy we can go with this card, but I am looking for a design that reflects a company that is comfortable with technology, policy, and having a little bit fun. I'm uploading my logo below, and I'd like to have it be part of the card design in some fashion.
Target Market(s)
Telecommunications and technology policy professionals
Industry/Entity Type
Technology policy
Contact Information for Business Card
Name of business, my name (Glen Mosswater), email (glen@corvellestrategies-example.com) , phone number (202-555-0148)phone number

```html
<!DOCTYPE html>
<html lang="en">
<head>
<meta charset="utf-8">
<title>Corvelle Strategies – Business Card</title>
<link rel="stylesheet" href="https://fonts.googleapis.com/css2?family=Cinzel:wght@400&family=Montserrat:wght@400;600;700&display=swap">
<style>
  :root {
    --brand-blue: #0a58a6;
    --accent-gold: #f4ad3d;
    --card-white: #ffffff;
    --stage: #e6e7e9;
    --text-blue: #0d4f98;
  }
  * { box-sizing: border-box; margin: 0; padding: 0; }
  html, body { width: 804px; height: 1200px; overflow: hidden; }
  body {
    background: var(--stage);
    position: relative;
    font-family: "Montserrat", sans-serif;
  }
  .card {
    position: absolute;
    left: 62px;
    width: 680px;
    height: 389px;
    border-radius: 22px;
    overflow: hidden;
    box-shadow: 0 8px 24px rgba(0,0,0,0.18);
  }
  .card--front { top: 150px; background: var(--card-white); }
  .card--back { top: 661px; background: var(--brand-blue); }

  .frame { position: absolute; inset: 0; }

  .wordmark {
    position: absolute;
    display: flex;
    align-items: center;
    gap: 14px;
    font-weight: 700;
    font-size: 42px;
    letter-spacing: 0.5px;
    white-space: nowrap;
  }
  .wordmark__dot {
    width: 30px; height: 30px;
    border-radius: 50%;
    background: var(--accent-gold);
    flex: none;
  }
  .card--front .wordmark { left: 70px; top: 70px; color: var(--brand-blue); }
  .card--back .wordmark { left: 110px; top: 130px; color: var(--card-white); }

  .holder {
    position: absolute;
    right: 70px;
    top: 170px;
    font-family: "Cinzel", serif;
    font-size: 25px;
    color: var(--text-blue);
    letter-spacing: 1px;
    padding-bottom: 4px;
    border-bottom: 2px solid var(--accent-gold);
  }
  .rule {
    position: absolute;
    left: 70px; top: 212px;
    width: 200px; height: 1px;
    background: var(--brand-blue);
  }

  .contact {
    position: absolute;
    left: 70px; top: 250px;
    list-style: none;
    color: var(--text-blue);
    font-size: 16px;
    line-height: 26px;
  }
  .contact li { display: flex; align-items: center; gap: 10px; }
  .contact svg { width: 15px; height: 15px; flex: none; }
  .contact__phone { font-weight: 700; }
  .contact__web strong { font-weight: 700; }

  .back-url {
    position: absolute;
    left: 0; right: 0;
    top: 250px;
    text-align: center;
    color: var(--card-white);
    font-size: 19px;
    letter-spacing: 5px;
  }
</style>
</head>
<body>

<section class="card card--front" aria-label="Business card front">
  <svg class="frame" viewBox="0 0 680 389" aria-hidden="true">
    <g fill="none" stroke="var(--brand-blue)">
      <rect x="30" y="30" width="620" height="329" stroke-width="2"/>
      <rect x="36" y="36" width="608" height="317" stroke-width="1"/>
    </g>
    <g fill="var(--accent-gold)">
      <circle cx="26" cy="26" r="12"/>
      <circle cx="654" cy="26" r="12"/>
      <circle cx="26" cy="363" r="12"/>
      <circle cx="654" cy="363" r="12"/>
    </g>
  </svg>

  <div class="wordmark"><span class="wordmark__dot"></span>Corvelle Strategies</div>

  <p class="holder">Glen Mosswater</p>
  <span class="rule"></span>

  <ul class="contact">
    <li class="contact__phone">
      <svg viewBox="0 0 24 24" fill="currentColor"><path d="M6.6 10.8a15.1 15.1 0 0 0 6.6 6.6l2.2-2.2a1 1 0 0 1 1-.25 11.4 11.4 0 0 0 3.6.57 1 1 0 0 1 1 1V20a1 1 0 0 1-1 1A17 17 0 0 1 3 4a1 1 0 0 1 1-1h3.5a1 1 0 0 1 1 1c0 1.25.2 2.45.57 3.57a1 1 0 0 1-.25 1z"/></svg>
      (202-555-0148)
    </li>
    <li>
      <svg viewBox="0 0 24 24" fill="none" stroke="currentColor" stroke-width="2"><rect x="3" y="5" width="18" height="14" rx="1"/><path d="M3 6l9 7 9-7"/></svg>
      glen@corvellestrategies-example.com
    </li>
    <li class="contact__web">
      <svg viewBox="0 0 24 24" fill="currentColor"><circle cx="12" cy="12" r="10"/></svg>
      <span>www.<strong>CorvelleStrategies</strong>-example.com</span>
    </li>
  </ul>
</section>

<section class="card card--back" aria-label="Business card back">
  <div class="wordmark"><span class="wordmark__dot"></span>Corvelle Strategies</div>
  <p class="back-url">www.CorvelleStrategies-example.com</p>
</section>

</body>
</html>
```